Melissa Dorvan Personal Business Card

I like orange. It's would better if my card have an orange background
Address: 5820 Halvers Lane #417
San Jose
California
US
Tel: 4085172049

Industry/Entity Type

Business

```html
<!DOCTYPE html>
<html lang="en">
<head>
<meta charset="utf-8">
<title>Melissa Dorvan – Business Card</title>
<link rel="stylesheet" href="https://fonts.googleapis.com/css2?family=Marcellus&family=Kalam:wght@400&display=swap">
<style>
  :root {
    --backdrop: #000000;
    --card-orange-light: #fbb217;
    --card-orange: #f57d12;
    --card-orange-deep: #ee5a14;
    --glow: #fff4c8;
    --bokeh: #ffd9b8;
    --ink: #ffffff;
  }
  html, body {
    margin: 0;
    padding: 0;
    width: 1200px;
    height: 900px;
    overflow: hidden;
    background: var(--backdrop);
  }
  .card {
    position: absolute;
    left: 60px;
    top: 140px;
    width: 1080px;
    height: 620px;
    overflow: hidden;
    background: radial-gradient(ellipse 90% 110% at 0% 60%, var(--card-orange-light) 0%, var(--card-orange) 55%, var(--card-orange-deep) 100%);
  }
  .card__decoration {
    position: absolute;
    right: -40px;
    bottom: -60px;
    width: 640px;
    height: 560px;
    background:
      radial-gradient(ellipse 60% 18% at 55% 45%, rgba(255, 244, 200, 0.55) 0%, rgba(255, 244, 200, 0) 70%),
      radial-gradient(ellipse 55% 45% at 60% 60%, rgba(255, 217, 184, 0.45) 0%, rgba(255, 217, 184, 0) 75%);
  }
  .card__name {
    position: absolute;
    top: 44px;
    right: 60px;
    margin: 0;
    font-family: "Marcellus", serif;
    font-size: 84px;
    font-weight: 400;
    letter-spacing: 1px;
    color: var(--ink);
    text-shadow: 0 2px 3px rgba(120, 40, 0, 0.35);
  }
  .card__contact {
    position: absolute;
    left: 70px;
    bottom: 50px;
    margin: 0;
    font-family: "Kalam", cursive;
    font-style: normal;
    font-size: 50px;
    line-height: 1.2;
    color: var(--ink);
  }
  .card__contact span {
    display: block;
  }
</style>
</head>
<body>
  <section class="card">
    <div class="card__decoration" role="img" aria-label="Glowing light swirls with soft white bokeh dots"></div>
    <h1 class="card__name">Melissa Dorvan</h1>
    <address class="card__contact">
      <span class="card__address">Address : 5820 Halvers Lane#417</span>
      <span class="card__city">san jose</span>
      <span class="card__region">California US</span>
      <span class="card__phone">Tel: 4085172049</span>
    </address>
  </section>
</body>
</html>
```